Reef Glow

sunglasses, sihoullette of body, maybe wearing a bikini or sunglasses. I am offering spray tanning, body wraps, tanning beds, stand up, body art, airbrush makeup.

Target Market(s)

I would say my target is all ages, But tanning is a seasonal business and more beauty and aging concept. and around prom time I get my most profitable business. so 18 to 21 through march and april. then 25 to 55 through april to june.

Industry/Entity Type

Makeup

Contact Information for Business Card

Phone number: 701-382-5147 Owner: Jan Mortby (Lisowski)

Colors

Designer to choose colors to be used in the design.

Requirements
Nice to have
• Sunglasses, silouttes of body wearing sunglasses or bikini, or picture of spray gun.

```html
<!DOCTYPE html>
<html lang="en">
<head>
<meta charset="utf-8">
<title>Reef Glow – Business Card</title>
<link rel="stylesheet" href="https://fonts.googleapis.com/css2?family=Advent+Pro:wght@200;300&family=Noto+Serif:wght@700&display=swap">
<style>
  :root {
    --page-bg: #2b2b2d;
    --card-base: #ece8ec;
    --card-shade: #ddd6dd;
    --name-plum: #9c5680;
    --phone-plum: #a56a90;
    --ink: #1e1e1e;
    --bikini-pink: #d98bc4;
    --skin-light: #f3ecef;
    --glow-gold: #e3c98a;
  }
  * { margin: 0; padding: 0; box-sizing: border-box; }
  html, body {
    width: 1200px;
    height: 800px;
    overflow: hidden;
    background: var(--page-bg);
  }
  .canvas {
    position: relative;
    width: 1200px;
    height: 800px;
    display: flex;
    align-items: center;
    justify-content: center;
  }
  .business-card {
    position: relative;
    width: 1050px;
    height: 600px;
    background:
      radial-gradient(ellipse at 30% 20%, #f4f1f4 0%, transparent 60%),
      radial-gradient(ellipse at 80% 90%, var(--card-shade) 0%, transparent 65%),
      var(--card-base);
    overflow: hidden;
  }
  .sun-glow {
    position: absolute;
    left: 280px;
    top: 150px;
    width: 380px;
    height: 380px;
    border-radius: 50%;
    background: radial-gradient(circle, #fbf6e8 0%, var(--glow-gold) 22%, rgba(227, 201, 138, 0.45) 45%, rgba(227, 201, 138, 0) 70%);
  }
  .figure-art {
    position: absolute;
    left: 70px;
    top: 50px;
    width: 250px;
    height: 540px;
    border-radius: 120px 120px 40px 40px;
    background: linear-gradient(180deg, var(--skin-light) 0%, #f1dfe9 35%, var(--bikini-pink) 60%, #efe3ea 100%);
    opacity: 0.75;
  }
  .owner-name {
    position: absolute;
    left: 545px;
    top: 52px;
    font-family: "Advent Pro", sans-serif;
    font-weight: 200;
    font-size: 64px;
    letter-spacing: 3px;
    color: var(--name-plum);
  }
  .owner-title {
    position: absolute;
    left: 655px;
    top: 138px;
    font-family: "Noto Serif", serif;
    font-weight: 700;
    font-size: 17px;
    letter-spacing: 1px;
    color: var(--ink);
  }
  .phone-line {
    position: absolute;
    left: 540px;
    top: 395px;
    display: flex;
    align-items: center;
    gap: 8px;
    font-family: "Advent Pro", sans-serif;
    font-weight: 200;
    font-size: 46px;
    letter-spacing: 4px;
    color: var(--phone-plum);
  }
  .phone-icon { width: 34px; height: 34px; }
</style>
</head>
<body>
  <main class="canvas">
    <article class="business-card">
      <div class="sun-glow"></div>
      <div class="figure-art" role="img" aria-label="Line drawing of a woman in a pink bikini"></div>
      <h1 class="owner-name">Jan Mortby</h1>
      <p class="owner-title">owner</p>
      <p class="phone-line">
        <svg class="phone-icon" viewBox="0 0 24 24" aria-hidden="true">
          <path fill="#1e1e1e" d="M6.6 3.2c.5-.4 1.2-.3 1.6.2l2.1 2.8c.4.5.3 1.2-.1 1.6L9 8.9c.9 2.3 2.7 4.2 5 5.1l1.1-1.2c.4-.4 1.1-.5 1.6-.1l2.8 2.1c.5.4.6 1.1.2 1.6l-1.4 1.8c-.7.9-1.9 1.3-3 .9C9.3 17.3 5.7 13.7 3.9 8.7c-.4-1.1 0-2.3.9-3z"/>
        </svg>
        <span>701-382-5147</span>
      </p>
    </article>
  </main>
</body>
</html>
```